REAL ESTATE MAILBOX DROP FLYER

I am looking for two flyer designs. One for DL and one for A4 size. My company is a boutique real estate agency that offers a full/high quality service at a very low commission rate.

Key Phrases to be included

A4 Design should have a space for some text and a table in the center (outline below)

Target Market(s)

Home Owners

Industry/Entity Type

Real Estate Agent

Colors
0455a3

Requirements
Must have
• Eye Catching
• Bold
• high end feel
• Color pallette should match the logo
• The feel of the brochures must convey a trustworthy, high end service.
• Must be eye catching and easy to read
• Editable file formats must be supplied

```html
<!DOCTYPE html>
<html lang="en">
<head>
<meta charset="UTF-8">
<title>Harbor Lane Property – Flyer</title>
<link href="https://fonts.googleapis.com/css2?family=Libre+Baskerville&family=Montserrat:wght@500;600;700&display=swap" rel="stylesheet">
<style>
  :root {
    --navy: #13244c;
    --navy-deep: #0e1b3a;
    --white: #ffffff;
    --page: #f2f2f2;
    --mist: #c9d0d3;
    --ink: #13244c;
  }
  * { margin: 0; padding: 0; box-sizing: border-box; }
  html, body { width: 1200px; height: 800px; overflow: hidden; background: var(--page); }
  .flyer {
    position: absolute; left: 331px; top: 20px;
    width: 538px; height: 760px;
    background: var(--white); overflow: hidden;
    font-family: "Montserrat", sans-serif; color: var(--ink);
  }
  .hero-photo {
    position: absolute; left: 0; top: 0; width: 538px; height: 256px;
    background: linear-gradient(180deg, #7fcfd8 0%, #b7dfe0 30%, #a8614a 45%, #e9e6e0 62%, #4e6a3a 85%, #6f8a3e 100%);
  }
  .brand-badge {
    position: absolute; left: 394px; top: -58px; width: 126px; height: 126px;
    border-radius: 50%; background: var(--white);
    display: flex; align-items: flex-end; justify-content: center; padding-bottom: 22px;
  }
  .brand-name {
    font-family: "Libre Baskerville", serif; font-weight: 400;
    text-transform: uppercase; text-align: center; line-height: 1.1;
    color: var(--navy); font-size: 12px; letter-spacing: .5px;
  }
  .headline-band {
    position: absolute; left: 0; top: 256px; width: 538px; height: 122px;
    background: var(--navy);
  }
  .agent-photo {
    position: absolute; left: 37px; top: 199px; width: 102px; height: 179px;
    border-radius: 50px 50px 0 0;
    background: linear-gradient(180deg, #e0b66a 0%, #d9a98a 30%, #2e2e33 60%, #24242a 100%);
  }
  .headline {
    position: absolute; left: 180px; width: 340px; text-align: center;
    font-family: "Libre Baskerville", serif; color: var(--white); text-transform: uppercase;
  }
  .headline-main { top: 288px; font-size: 31px; letter-spacing: 2px; }
  .headline-sub { top: 330px; font-size: 18px; letter-spacing: 1px; }
  .about-photo {
    position: absolute; left: 0; top: 378px; width: 538px; height: 300px;
    background: linear-gradient(160deg, #e8e2de 0%, #f5f3f1 35%, #ece6e2 60%, #f7f7f7 100%);
  }
  .section-title {
    position: absolute; left: 0; width: 538px; top: 424px; text-align: center;
    font-size: 27px; font-weight: 700; letter-spacing: 1.5px;
  }
  .feature { position: absolute; }
  .feature h3 { font-size: 15.5px; font-weight: 600; letter-spacing: 1px; text-transform: uppercase; margin-bottom: 5px; }
  .feature p { font-size: 8.6px; font-weight: 600; line-height: 12.5px; text-transform: uppercase; }
  .feature-service { left: 26px; top: 480px; width: 240px; }
  .feature-commission { left: 329px; top: 478px; width: 200px; }
  .feature-savings { left: 97px; top: 574px; width: 360px; }
  .feature-savings p { padding-left: 36px; }
  .footer-wave { position: absolute; left: 0; top: 640px; width: 538px; height: 120px; }
  .footer-brand { position: absolute; left: 20px; top: 694px; }
  .footer-brand .brand-name { color: var(--white); font-size: 19px; text-align: left; }
  .contact { position: absolute; left: 331px; top: 723px; display: flex; align-items: center; gap: 20px; }
  .contact-number { color: var(--white); font-size: 18.5px; font-weight: 600; letter-spacing: 2px; }
</style>
</head>
<body>
  <main class="flyer">
    <div class="hero-photo" role="img" aria-label="Photo of a large Tudor-style family home with red tiled roof and green lawn"></div>
    <div class="brand-badge"><span class="brand-name">Harbor Lane<br>Property</span></div>

    <div class="headline-band"></div>
    <div class="agent-photo" role="img" aria-label="Photo of a smiling real estate agent in a dark blazer, arms crossed"></div>
    <h1 class="headline headline-main">Trustworthy</h1>
    <h2 class="headline headline-sub">High End Service Agency</h2>

    <div class="about-photo" role="img" aria-label="Faded photo of a hand passing house keys over a signed contract"></div>
    <h2 class="section-title">ABOUT US</h2>

    <section class="feature feature-service">
      <h3>Full Service Agency</h3>
      <p>Lorem ipsum dolor sit amet,con-<br>sectetur adipiscing elit .lorem<br>ipsum dolor sit amet,consecte-<br>tur adipiscing elit</p>
    </section>
    <section class="feature feature-commission">
      <h3>1% Commission</h3>
      <p>Lorem ipsum dolor sit amet,con-<br>sectetur adipiscing elit .lorem<br>ipsum dolor sit amet,consecte-<br>tur adipiscing elit</p>
    </section>
    <section class="feature feature-savings">
      <h3>Save Thousands on Commision</h3>
      <p>Lorem ipsum dolor sit amet,consectetur<br>adipiscing elit .lorem ipsum dolor sit amet,-<br>consectetur adipiscing elit</p>
    </section>

    <svg class="footer-wave" viewBox="0 0 538 120" aria-hidden="true">
      <path d="M0 28 C120 -4 260 48 538 76 L538 120 L0 120 Z" fill="var(--mist)"/>
      <path d="M0 32 C110 10 250 64 400 70 C470 72 510 66 538 62 L538 120 L0 120 Z" fill="var(--navy)"/>
    </svg>

    <div class="footer-brand"><span class="brand-name">Harbor Lane<br>Property</span></div>

    <div class="contact">
      <svg width="26" height="30" viewBox="0 0 26 30" aria-hidden="true">
        <rect x="0" y="0" width="26" height="30" rx="5" fill="var(--white)"/>
        <path d="M9 6 C7 7 6 9 6 12 C7 18 11 23 15 25 C17 26 19 25 20 23 L17 20 L15 22 C12 20 10 16 10 13 L12 11 Z" fill="var(--navy)"/>
      </svg>
      <span class="contact-number">0400 123 567</span>
    </div>
  </main>
</body>
</html>
```